Political Mail Out Quintero front and back

Front
Esteban (9th Grade) Quintero!

What's that famous saying?

Show me who your friends are and I'll tell you who you really are!
(show the two guys)

Arturo Benavides is charged with voter fraud by changing voter addresses from across the RGV so they could vote in Edinburg
Back
Did Esteban (9th Grade) Quintero commit voter fraud when he ran for office in 2016?
(insert blurred photo)

Here is a list of people from all over the RGV that voted in Edinburg in the 2016 race.
Here is a break down:

(highlight the number and where they were first registered to vote)

9 People voted in Edinburg who were registered in Donna.
13 People voted in Edinburg who were registered in San Juan
8 People voted in Edinburg who were registered in Pharr
31 People voted in Edinburg who were registered in McAllen
2 People voted in Edinburg who were registered in La Joya
6 People voted in Edinburg who were registered in Edcouch
2 People voted in Edinburg who were registered in Mercedes
2 People voted in Edinburg who were registered in Monte Alto
6 People voted in Edinburg who were registered in Weslaco
1 Person voted in Edinburg who were registered in Penitas
3 People voted in Edinburg who were registered in Alamo
5 People voted in Edinburg who were registered in Elsa
6 People voted in Edinburg who were registered in Mission
1 Person voted in Edinburg who were registered in Alton

Will Esteban (9th Grade) Quintero CHEAT in 2020?

Only time will tell.

Vote Esteban (9th Grade) Quintero OUT of office.

```html
<!DOCTYPE html>
<html lang="en">
<head>
<meta charset="utf-8">
<title>Quintero Mail Out – Front and Back</title>
<link href="https://fonts.googleapis.com/css2?family=Bebas+Neue&family=Lato:wght@400;700;900&display=swap" rel="stylesheet">
<style>
  :root{
    --bg:#c3c5d1;
    --blue:#2566d0;
    --blue-dark:#1b4fa8;
    --red:#d0161b;
    --red-dark:#8e0c10;
    --black:#111111;
    --gray:#454545;
    --white:#ffffff;
    --doc:#c7c8c2;
  }
  *{box-sizing:border-box;margin:0;padding:0}
  html,body{width:1200px;height:1200px;overflow:hidden;background:var(--bg);font-family:"Lato",sans-serif}
  .mailer{position:absolute;width:530px;height:662px;background:var(--white);overflow:hidden;box-shadow:0 14px 26px rgba(0,0,0,.35)}
  .mailer--front{left:48px;top:113px}
  .mailer--back{left:620px;top:373px}
  .top-stripe{position:absolute;left:0;top:0;width:100%;height:6px;background:var(--red)}

  /* FRONT */
  .name-block{position:absolute;left:0;top:6px;width:207px;height:116px;padding:12px 0 0 16px;color:var(--blue-dark);font-family:"Bebas Neue",sans-serif;font-weight:400;line-height:.9}
  .name-block .first{font-size:62px;display:block}
  .name-block .grade{font-size:41px;display:block}
  .surname-block{position:absolute;left:207px;top:6px;width:323px;height:116px;background:var(--blue)}
  .surname-block text{font-family:"Bebas Neue",sans-serif;fill:var(--white)}
  .saying-bar{position:absolute;left:0;top:122px;width:100%;height:43px;background:var(--black);color:var(--white);font-weight:700;font-size:23px;text-align:center;line-height:43px}
  .ribbons{position:absolute;left:0;top:165px}
  .ribbons text{font-family:"Lato",sans-serif;font-weight:900;fill:var(--white)}
  .friends-photo{position:absolute;left:0;top:432px;width:530px;height:230px;background:var(--black)}
  .friends-photo .photo{position:absolute;left:0;top:0;width:330px;height:230px;background:linear-gradient(120deg,#2b231c,#6a5440 45%,#3b3027)}
  .warning{position:absolute;left:446px;top:418px}
  .charge-box{position:absolute;left:249px;top:477px;width:258px;height:102px;border:2px solid var(--red);background:var(--black);color:var(--white);font-size:14px;line-height:17.5px;text-align:center;padding:6px 4px;white-space:nowrap}
  .swoosh{position:absolute;left:0;top:560px}

  /* BACK */
  .question-bar{position:absolute;left:0;top:6px;width:100%;height:56px;background:var(--blue);color:var(--white);font-weight:700;font-size:16.5px;line-height:20px;text-align:center;padding-top:8px}
  .voter-list-photo{position:absolute;left:16px;top:74px;width:143px;height:328px;background:linear-gradient(90deg,#bdbeb8,var(--doc) 40%,#d6d6d0)}
  .breakdown{position:absolute;left:174px;top:72px;width:340px;height:330px;border:2px solid var(--red)}
  .breakdown .intro{height:80px;background:var(--red);color:var(--white);font-weight:700;font-size:16px;line-height:20px;text-align:center;padding-top:9px}
  .breakdown .heading{height:37px;background:var(--black);color:var(--white);font-weight:700;font-size:16px;line-height:37px;text-align:center}
  .breakdown ul{list-style:none;padding:8px 0 0 5px;font-size:11.6px;line-height:13.8px;color:var(--black)}
  .breakdown .num{color:var(--blue);display:inline-block;width:16px}
  .breakdown .town{color:var(--blue)}
  .cheat-question{position:absolute;left:16px;top:412px}
  .cheat-question .lead{color:var(--blue);font-weight:900;font-size:18px;line-height:22px}
  .cheat-question .big{color:var(--red);font-weight:900;font-size:31px;line-height:34px}
  .cheat-question .tell{color:var(--black);font-weight:700;font-size:16.5px;line-height:20px}
  .vote-ribbons{position:absolute;left:0;top:480px}
  .vote-ribbons text{font-family:"Lato",sans-serif;font-weight:900;fill:var(--white)}
</style>
</head>
<body>

<section class="mailer mailer--front">
  <div class="top-stripe"></div>
  <h1 class="name-block"><span class="first">ESTEBAN</span><span class="grade">(9TH GRADE)</span></h1>
  <svg class="surname-block" width="323" height="116" viewBox="0 0 323 116">
    <text x="14" y="100" font-size="104" textLength="296" lengthAdjust="spacingAndGlyphs">QUINTERO!</text>
  </svg>
  <div class="saying-bar">What’s That Famous Saying?...</div>

  <svg class="ribbons" width="530" height="267" viewBox="0 0 530 267">
    <g transform="rotate(-8 265 130)">
      <polygon points="160,190 200,190 215,250" fill="var(--black)"/>
      <polygon points="45,64 90,64 90,86" fill="var(--red-dark)"/>
      <rect x="80" y="64" width="360" height="88" fill="var(--gray)"/>
      <rect x="30" y="24" width="200" height="42" fill="var(--red)"/>
      <text x="46" y="56" font-size="30">SHOW ME</text>
      <text x="96" y="100" font-size="26">WHO YOUR FRIENDS ARE</text>
      <text x="96" y="132" font-size="26">AND I’LL TELL YOU</text>
      <rect x="170" y="144" width="380" height="48" fill="var(--blue)"/>
      <text x="190" y="179" font-size="29">WHO YOU REALLY ARE!</text>
      <rect x="220" y="198" width="330" height="3" fill="var(--red)"/>
      <rect x="220" y="204" width="330" height="3" fill="var(--blue)"/>
    </g>
  </svg>

  <div class="friends-photo">
    <div class="photo" role="img" aria-label="Photo of Esteban Quintero standing with Arturo Benavides"></div>
  </div>
  <svg class="swoosh" width="530" height="102" viewBox="0 0 530 102">
    <defs>
      <linearGradient id="swooshFill" x1="0" x2="1">
        <stop offset="0" stop-color="var(--blue)"/>
        <stop offset=".45" stop-color="#6a3a9a"/>
        <stop offset=".7" stop-color="var(--red)"/>
        <stop offset="1" stop-color="var(--red-dark)"/>
      </linearGradient>
    </defs>
    <polygon points="0,60 530,0 530,102 0,102" fill="url(#swooshFill)"/>
    <polygon points="0,85 530,38 530,102 0,102" fill="var(--blue)" opacity=".55"/>
  </svg>
  <svg class="warning" width="60" height="54" viewBox="0 0 60 54" aria-hidden="true">
    <polygon points="30,2 58,52 2,52" fill="var(--red)"/>
    <rect x="27" y="18" width="6" height="20" rx="2" fill="var(--white)"/>
    <circle cx="30" cy="44" r="3.5" fill="var(--white)"/>
  </svg>
  <p class="charge-box">ARTURO BENAVIDES<br>is charged with VOTER FRAUD<br>by changing voter addresses from<br>across the RGV so they could vote<br>in Edinburg</p>
</section>

<section class="mailer mailer--back">
  <div class="top-stripe"></div>
  <h2 class="question-bar">DID ESTEBAN (9TH GRADE) QUINTERO COMMIT VOTER FRAUD<br>WHEN HE RAN FOR OFFICE IN 2016?</h2>
  <div class="voter-list-photo" role="img" aria-label="Blurred photo of the printed voter list"></div>

  <div class="breakdown">
    <p class="intro">Here is a list of people<br>from all over the RGV that voted<br>in Edinburg in the 2016 race.</p>
    <p class="heading">HERE IS THE BREAK DOWN</p>
    <ul>
      <li><span class="num">9</span>People voted in Edinburg who were registered in <span class="town">Donna.</span></li>
      <li><span class="num">13</span>People voted in Edinburg who were registered in <span class="town">San Juan</span></li>
      <li><span class="num">8</span>People voted in Edinburg who were registered in <span class="town">Pharr</span></li>
      <li><span class="num">31</span>People voted in Edinburg who were registered in <span class="town">McAllen</span></li>
      <li><span class="num">2</span>People voted in Edinburg who were registered in <span class="town">La Joya</span></li>
      <li><span class="num">6</span>People voted in Edinburg who were registered in <span class="town">Edcouch</span></li>
      <li><span class="num">2</span>People voted in Edinburg who were registered in <span class="town">Mercedes</span></li>
      <li><span class="num">2</span>People voted in Edinburg who were registered in <span class="town">Monte Alto</span></li>
      <li><span class="num">6</span>People voted in Edinburg who were registered in <span class="town">Weslaco</span></li>
      <li><span class="num">1</span>Person voted in Edinburg who were registered in <span class="town">Penitas</span></li>
      <li><span class="num">3</span>People voted in Edinburg who were registered in <span class="town">Alamo</span></li>
      <li><span class="num">5</span>People voted in Edinburg who were registered in <span class="town">Elsa</span></li>
      <li><span class="num">6</span>People voted in Edinburg who were registered in <span class="town">Mission</span></li>
      <li><span class="num">1</span>Person voted in Edinburg who were registered in <span class="town">Alton</span></li>
    </ul>
  </div>

  <div class="cheat-question">
    <p class="lead">WILL ESTEBAN (9TH GRADE) QUINTERO</p>
    <p class="big">CHEAT IN 2020?</p>
    <p class="tell">Only Time Will Tell...</p>
  </div>

  <svg class="vote-ribbons" width="530" height="182" viewBox="0 0 530 182">
    <circle cx="50" cy="142" r="62" fill="none" stroke="var(--red)" stroke-width="3"/>
    <g fill="none" stroke="var(--blue)" stroke-width="3" stroke-linejoin="round">
      <rect x="56" y="97" width="14" height="30" rx="2"/>
      <path d="M56 100 H34 q-6 0-7 6 l-4 18 q-1 6 5 6 h12 l-3 12 q-1 7 5 8 l12-20 v-30"/>
    </g>
    <g stroke="var(--red)" stroke-width="2.5" stroke-linecap="round">
      <line x1="36" y1="160" x2="32" y2="166"/><line x1="44" y1="162" x2="44" y2="169"/><line x1="52" y1="160" x2="56" y2="166"/>
    </g>
    <g transform="rotate(-8 300 90)">
      <polygon points="140,95 170,95 180,130" fill="var(--blue-dark)"/>
      <polygon points="330,158 380,158 410,196" fill="var(--red-dark)"/>
      <rect x="130" y="62" width="330" height="54" fill="var(--gray)"/>
      <rect x="110" y="40" width="118" height="42" fill="var(--blue)"/>
      <text x="122" y="73" font-size="30">VOTE</text>
      <text x="144" y="103" font-size="22" textLength="300" lengthAdjust="spacingAndGlyphs">ESTEBAN 9TH GRADE QUINTERO</text>
      <rect x="236" y="118" width="304" height="44" fill="var(--red)"/>
      <text x="250" y="150" font-size="27" textLength="270" lengthAdjust="spacingAndGlyphs">OUT OF THE OFFICE!</text>
      <rect x="270" y="168" width="280" height="3" fill="var(--red)"/>
      <rect x="270" y="174" width="280" height="3" fill="var(--blue)"/>
    </g>
  </svg>
</section>

</body>
</html>
```